Convert my PowerPoint mock up of a hiring process flow to simple, informative illustration with some

I need to create an illustration which is meant to be an overview of a hiring process for a medical training start up. I created a pretty rough PowerPoint mock up that hopefully shows what I am trying to do. My hope is that I would get the illustration created and can add it to my website. I have several other similar projects needed as well and probably ongoing graphic design work if we develop a good working relationship.

Site: www.brolvanhealth.com

Target Market(s)

Medical employers

Industry/Entity Type

Healthcare

Number of Pages Required

1 page

Font styles to use
Serif
Sans Serif

Colors
2fb6a2
85cae6

Requirements
Must have
• Simple illustration when done
Nice to have
• Fits very well with existing look and feel of site.
Should not have
• Not sure

```html
<!DOCTYPE html>
<html lang="en">
<head>
<meta charset="utf-8">
<title>Brolvan Hiring Process</title>
<link href="https://fonts.googleapis.com/css2?family=Roboto:wght@400;500&display=swap" rel="stylesheet">
<style>
:root{
  --navy:#0b4a86;
  --navy-dark:#083c6e;
  --teal:#2fb6a2;
  --panel:#dde9f3;
  --header:#f7f7f7;
  --ink:#444b52;
  --page-blue:#0a6fbd;
  --white:#ffffff;
}
*{margin:0;padding:0;box-sizing:border-box}
html,body{width:1200px;height:885px;overflow:hidden}
body{
  font-family:'Roboto',Arial,sans-serif;
  background:linear-gradient(135deg,#0c7dcc 0%,#0a66b3 45%,#0b78c6 75%,#0863ad 100%);
  position:relative;color:var(--ink);
}
.abs{position:absolute}
.card{left:99px;top:38px;width:1003px;height:746px;background:var(--white)}
.header{left:99px;top:38px;width:1003px;height:121px;background:var(--header);border-bottom:2px solid #e6ecf1}
.panel{left:99px;top:161px;width:1003px;height:609px;background:var(--panel)}
.brand{left:121px;top:45px;width:204px;height:87px;background:var(--white);display:flex;align-items:center;justify-content:center;gap:8px}
.brand-mark{width:26px;height:26px;border-radius:50%;background:var(--navy)}
.brand-name{font-size:22px;font-weight:500;color:var(--navy);letter-spacing:.5px}
.login{left:969px;top:80px;width:92px;height:37px;background:var(--navy);border-radius:4px;color:#fff;font-size:14px;display:flex;align-items:center;justify-content:center;letter-spacing:.5px}
.tag{top:206px;width:62px;height:53px;background:var(--teal);color:#fff;font-size:16px;display:flex;align-items:center;justify-content:center}
.tag--active{background:#000}
.caption{width:330px;left:150px;text-align:center;font-size:15.5px;line-height:22px;color:var(--ink)}
.note{left:151px;top:388px;width:327px;height:155px;background:#fff;border:1px solid #d3dde6;padding:22px 20px;font-size:11px;line-height:22px;text-align:justify;text-align-last:center;color:#4a4a4a}
.photo{height:78px;border:1px solid var(--teal)}
.photo--warm{background:linear-gradient(160deg,#d9d2c8,#8a6a55)}
.photo--cool{background:linear-gradient(160deg,#dedede,#6f6a66)}
.step{left:605px;width:451px;color:#fff;display:flex;align-items:center;justify-content:center;text-transform:uppercase}
.step--navy{background:var(--navy)}
.step--teal{background:var(--teal)}
.bar{background:linear-gradient(180deg,var(--navy) 0%,var(--navy-dark) 100%);color:#fff;display:flex;align-items:center;justify-content:center;text-transform:uppercase;letter-spacing:.5px}
.training{left:605px;top:531px;width:451px;height:69px;background:linear-gradient(180deg,#4a4f57 0%,#2d3138 60%,#1f242b 100%);color:#fff;font-size:17.5px;display:flex;align-items:center;justify-content:center;letter-spacing:.5px}
.footer-text{left:107px;top:823px;font-size:14px;color:#fff}
.social{top:820px;width:32px;height:32px;border:1px solid rgba(255,255,255,.8);border-radius:50%}
</style>
</head>
<body>
<div class="abs card"></div>
<header class="abs header"></header>
<div class="abs brand"><span class="brand-mark"></span><span class="brand-name">BROLVAN</span></div>
<div class="abs login">LOGIN</div>
<div class="abs panel"></div>

<div class="abs tag tag--active" style="left:151px">CSV</div>
<div class="abs tag" style="left:218px">CSV</div>
<div class="abs tag" style="left:284px">CSV</div>
<div class="abs tag" style="left:350px">CSV</div>
<div class="abs tag" style="left:417px">CSV</div>

<p class="abs caption" style="top:279px">Collect and Synthesize Candidates<br>for Training, Employment</p>

<svg class="abs" style="left:300px;top:338px" width="30" height="34" viewBox="0 0 30 34"><path d="M15 1V32M5 22L15 32 25 22" fill="none" stroke="var(--navy)" stroke-width="1.3"/></svg>

<div class="abs note">Lorem ipsum dolor sit amet, consectetur adipiscing elit, sed do eiusmod tempor incididunt ut labore et dolore magna aliqua. Ut enim ad minim veniam, quis nostrud exercitation ullamco laboris nisi ut aliquip ex ea commodo consequat. Duis aute irure dolor</div>

<p class="abs caption" style="top:579px">Employer selects their favored<br>candidates to interview</p>

<div class="abs photo photo--warm" style="left:150px;top:643px;width:62px" role="img" aria-label="Candidate portrait"></div>
<div class="abs photo photo--cool" style="left:217px;top:643px;width:62px" role="img" aria-label="Candidate portrait"></div>
<div class="abs photo photo--warm" style="left:284px;top:643px;width:62px" role="img" aria-label="Candidate portrait"></div>
<div class="abs photo photo--warm" style="left:351px;top:643px;width:62px" role="img" aria-label="Candidate portrait"></div>
<div class="abs photo photo--cool" style="left:417px;top:643px;width:62px" role="img" aria-label="Candidate portrait"></div>

<svg class="abs" style="left:530px;top:418px" width="36" height="106" viewBox="0 0 36 106"><path d="M2 2L33 53 2 104" fill="none" stroke="var(--navy)" stroke-width="1.2"/></svg>

<div class="abs step step--navy" style="top:197px;height:53px;font-size:14px;letter-spacing:.3px">Employer, Brolvan agree upon training protocol</div>
<svg class="abs" style="left:815px;top:251px" width="30" height="32" viewBox="0 0 30 32"><path d="M15 0V30M5 20L15 30 25 20" fill="none" stroke="var(--navy)" stroke-width="1.3"/></svg>
<div class="abs step step--teal" style="top:292px;height:54px;font-size:15.5px;letter-spacing:.4px">Candidates interviewed by employer</div>

<div class="abs photo photo--warm" style="left:605px;top:368px;width:85px" role="img" aria-label="Interview candidate portrait"></div>
<div class="abs photo photo--cool" style="left:697px;top:368px;width:85px" role="img" aria-label="Interview candidate portrait"></div>
<div class="abs photo photo--warm" style="left:788px;top:368px;width:85px;background:linear-gradient(160deg,#f1ece4,#c9a98a)" role="img" aria-label="Interview candidate portrait"></div>
<svg class="abs" style="left:916px;top:378px" width="20" height="60" viewBox="0 0 20 60"><path d="M2 2L18 30 2 58" fill="none" stroke="var(--navy)" stroke-width="1.1"/></svg>
<div class="abs photo photo--warm" style="left:971px;top:368px;width:85px" role="img" aria-label="Finalist portrait"></div>

<div class="abs bar" style="left:605px;top:464px;width:268px;height:43px;font-size:16px">Interviews</div>
<div class="abs bar" style="left:974px;top:464px;width:82px;height:43px;font-size:14px">Finalist</div>

<div class="abs training" role="img" aria-label="City skyline at dusk behind training heading">BROLVAN PRE-EMPLOYMENT TRAINING</div>

<div class="abs bar" style="left:767px;top:627px;width:127px;height:38px;font-size:16px">Start job!</div>

<div class="abs step step--teal" style="top:687px;height:54px;font-size:15.5px;letter-spacing:.4px">Post employment support (1-3 months)</div>

<footer>
<p class="abs footer-text">Copyright © brolvanhealth, All rights reserved</p>
<span class="abs social" style="left:971px" aria-label="Social link"></span>
<span class="abs social" style="left:1018px" aria-label="Social link"></span>
<span class="abs social" style="left:1066px" aria-label="Social link"></span>
</footer>
</body>
</html>
```